Brochure for an Online Sport Booking Website

We need a brochure design for a new company based in Bahrain called "GrassLoop.net".

GrassLoop is an online booking service for the sport field in Bahrain. We would like to design a brochure for the "partners" or clubs in away that reflects our idea and the type of customers who will benefit from the service. You can visit the website in order to get an idea about the service provided.

Service Description:
1. Share your sport facility details and calendar to attract more customers and enable them to book online
2. Book the pitch or activity on behalf of your customers over the website or using a smart phone
3. Manage the bookings in an efficient and effective manner
4. Secure your cash collection by receiving the payments in advance
5. Have the flexibility to change the rates and charges of pitches or activities based on different days and times
6. Receive Email and SMS notifications whenever there is a booking done by a customer
7. See your calendar updated automatically whenever a reservation is done online
8. Generate various reports that show the booking performance as well as generated revenue for any period of time
9. Improve and enhance the facility booking process by fully automating it
10. Launch and manage marketing campaign in order to increase sales through the website
11. Get the opportunity to host and organize tournaments in cooperation with GrassLoop.net
12. Identify and target customers to interact with them through social media tools integrated to the website (i.e.: FriendHub & SnapGrid)
13. Diversify the customer segments to avoid the dependency on certain customers

* We would like the design to use the color green as a background, nice and casual visual icons and images to show the above steps. The final design should communicate the value and benefits in a joyful and casual way that is attractive to the sport lovers.

* We need the design to be for 6 sided brochure with size of A4 (3 faces front and 3 back). Please refer to the attached file for more information about the content of the brochure.

* There should be a place somewhere in the brochure to show the games that are applicable:

Football, Basketball, Volleyball, Badmintor, Tinnes, Swimming Pools, Squash, Water Sports, etc. Ideally, logos or icons to be replacing the names of the games.

* We like to have a powerpoint presentation also along with the brochure.
* The winner will be chosen for more other futuristic desings.
Updates

Target Market(s)

Sport Clubs (Hotels, private and public clubs)

Industry/Entity Type

Marketing

Requirements
Nice to have
• logos, icons, images
Should not have
• Text only.

```html
<!DOCTYPE html>
<html lang="en">
<head>
<meta charset="utf-8">
<title>GrassLoop.net – Partner Brochure</title>
<link href="https://fonts.googleapis.com/css2?family=Bebas+Neue&family=Arimo:wght@400;700&display=swap" rel="stylesheet">
<style>
  :root{
    --green-deep:#17692f;
    --green-mid:#2f8a3a;
    --green-light:#6cb83c;
    --lime:#c8dc2a;
    --lime-text:#e3ef8a;
    --white:#ffffff;
    --icon:#e6efe6;
    --sea-dark:#1e5f86;
    --sea-light:#5fa6c6;
    --thumb:#d9e6b0;
  }
  html,body{margin:0;padding:0;overflow:hidden;}
  body{width:1200px;height:848px;}
  .brochure{
    position:relative;width:1200px;height:848px;overflow:hidden;
    background:linear-gradient(100deg,var(--green-deep) 0%,var(--green-mid) 45%,var(--green-light) 100%);
    font-family:"Arimo",Arial,sans-serif;color:var(--white);
  }
  .swoosh{position:absolute;left:0;top:0;width:1200px;height:848px;}
  .panel-title{
    position:absolute;margin:0;font-family:"Bebas Neue",Impact,sans-serif;
    font-weight:400;font-size:33px;letter-spacing:.5px;line-height:1;
  }
  .benefit{position:absolute;left:28px;width:340px;display:flex;gap:20px;}
  .benefit svg{flex:0 0 52px;height:52px;}
  .benefit p{margin:0;font-size:12.5px;line-height:1.05;text-align:justify;}
  .simply{position:absolute;left:431px;top:97px;font-size:13px;margin:0;}
  .step{position:absolute;left:422px;width:360px;height:69px;display:flex;align-items:center;}
  .step .screen{
    width:116px;height:69px;border-radius:5px;flex:0 0 116px;
    background:linear-gradient(180deg,#5c7a2d 0 12%,#9fc25a 12% 40%,var(--thumb) 40% 100%);
    box-shadow:0 4px 6px rgba(0,0,0,.25);
  }
  .step p{margin:0 0 0 44px;font-size:12.5px;line-height:1.05;}
  .discover{position:absolute;left:817px;top:103px;width:353px;font-size:12.5px;line-height:1.05;text-align:justify;}
  .discover p{margin:0 0 5px;}
  .tagline{position:absolute;left:817px;top:357px;margin:0;font-family:"Bebas Neue",Impact,sans-serif;font-size:22px;color:var(--lime-text);font-weight:400;}
</style>
</head>
<body>
<main class="brochure">
  <svg class="swoosh" viewBox="0 0 1200 848" aria-hidden="false">
    <defs>
      <linearGradient id="sea" x1="0" y1="0" x2="0" y2="1">
        <stop offset="0" stop-color="#9cc7d3"/>
        <stop offset="0.35" stop-color="var(--sea-light)"/>
        <stop offset="1" stop-color="var(--sea-dark)"/>
      </linearGradient>
    </defs>
    <path d="M460 848 C620 560 905 400 1200 382 L1200 848 Z" fill="#1b6b2e"/>
    <path d="M500 848 C650 575 920 420 1200 396" fill="none" stroke="var(--lime)" stroke-width="9"/>
    <path d="M512 848 C662 584 928 432 1200 410" fill="none" stroke="var(--white)" stroke-width="13"/>
    <path d="M524 848 C672 594 935 444 1200 420 L1200 848 Z" fill="url(#sea)" role="img" aria-label="Photo: two people paddling a kayak on blue sea water"/>
  </svg>

  <!-- Panel: why team up -->
  <h2 class="panel-title" style="left:27px;top:44px">Why team up with us?</h2>

  <div class="benefit" style="top:100px">
    <svg viewBox="0 0 52 52" fill="none" stroke="var(--icon)" stroke-width="2.5"><rect x="4" y="4" width="30" height="38"/><path d="M10 14h18M10 21h18M10 28h10"/><circle cx="40" cy="30" r="6" fill="var(--icon)"/><path d="M30 50c0-8 4-12 10-12s10 4 10 12z" fill="var(--icon)"/></svg>
    <p>1- Compete with the elite<br>Offer your facilities and services amongst sport centers in Bahrain and across the region.</p>
  </div>
  <div class="benefit" style="top:195px">
    <svg viewBox="0 0 52 52" fill="none" stroke="var(--icon)" stroke-width="3"><ellipse cx="20" cy="18" rx="16" ry="12"/><path d="M10 28l-4 8 10-5"/><path d="M26 32c2 6 8 9 14 8l6 4-1-7c4-3 5-9 2-13"/></svg>
    <p>2- Boost communication<br>Receive emails and SMS notifications on your calendar instantly when a reservation is made, changed or cancelled.</p>
  </div>
  <div class="benefit" style="top:298px">
    <svg viewBox="0 0 52 52" fill="none" stroke="var(--icon)" stroke-width="2.8"><rect x="6" y="22" width="9" height="24"/><path d="M15 24l9-10 3-10c4 0 6 4 4 10l-2 6h14c3 0 5 3 4 6l-4 16c-1 3-3 4-6 4H15"/></svg>
    <p>3- Rely on an efficient process with easy management<br>Simplify your booking management via your personalized online account in less time and effort.</p>
  </div>
  <div class="benefit" style="top:412px">
    <svg viewBox="0 0 52 52" fill="none" stroke="var(--icon)" stroke-width="2.5"><circle cx="26" cy="20" r="13"/><path d="M23 15l4-3v16" stroke-width="3.5"/><path d="M8 16c-2 10 2 22 12 28M44 16c2 10-2 22-12 28"/><path d="M18 50l8-6 8 6"/></svg>
    <p>4- Get exposure with a higher bottom line<br>Diversify your client base and maintain your steady income streak.</p>
  </div>
  <div class="benefit" style="top:502px">
    <svg viewBox="0 0 52 52" fill="none" stroke="var(--icon)" stroke-width="3"><path d="M44 26a19 19 0 1 1-6-14"/><path d="M40 4v9h-9"/><text x="26" y="32" fill="var(--icon)" stroke="none" font-family="Arimo,sans-serif" font-weight="700" font-size="16" text-anchor="middle">24</text></svg>
    <p>5- Gain Instant access anywhere anytime<br>Fully automate your booking list details from one website anywhere anytime.</p>
  </div>
  <div class="benefit" style="top:592px">
    <svg viewBox="0 0 52 52" fill="var(--icon)"><rect x="2" y="6" width="34" height="22" rx="2" transform="rotate(-12 19 17)"/><ellipse cx="38" cy="34" rx="11" ry="4"/><ellipse cx="38" cy="41" rx="11" ry="4"/><ellipse cx="38" cy="48" rx="11" ry="4"/></svg>
    <p>6- Guarantee your payments<br>Manage your bills instantly while your customers pay in advance or set your own payment rules.</p>
  </div>
  <div class="benefit" style="top:692px">
    <svg viewBox="0 0 52 52" fill="var(--icon)"><circle cx="12" cy="12" r="5"/><circle cx="26" cy="10" r="6"/><circle cx="40" cy="12" r="5"/><rect x="5" y="19" width="14" height="20" rx="3"/><rect x="18" y="18" width="16" height="24" rx="3"/><rect x="33" y="19" width="14" height="20" rx="3"/></svg>
    <p>7- Manage your work force<br>Eliminate and minimize human error and delays.</p>
  </div>

  <!-- Panel: join -->
  <h2 class="panel-title" style="left:429px;top:44px">Act now and join our network!</h2>
  <p class="simply">Simply,</p>
  <div class="step" style="top:116px"><div class="screen" role="img" aria-label="Website screenshot: sign-up page"></div><p>Sign up on GrassLoop.net</p></div>
  <div class="step" style="top:207px"><div class="screen" role="img" aria-label="Website screenshot: profile page"></div><p>Set up a profile for your sports<br>center or facility</p></div>
  <div class="step" style="top:305px"><div class="screen" role="img" aria-label="Website screenshot: services list"></div><p>List your services, prices and rules</p></div>
  <div class="step" style="top:404px"><div class="screen" role="img" aria-label="Website screenshot: fee plans"></div><p>Select the fee plan that best suits you</p></div>
  <div class="step" style="top:502px"><div class="screen" role="img" aria-label="Website screenshot: booking calendar"></div><p style="margin-left:40px;margin-top:-24px">Relax and allow<br>your calendar<br>to get filled up</p></div>

  <!-- Panel: discover -->
  <h2 class="panel-title" style="left:817px;top:44px">Discover more</h2>
  <div class="discover">
    <p>Our website offers you even more benefits. By signing up, you will be able to:</p>
    <p>1. Book your facilities or services on behalf of your customer online via a smart phone.</p>
    <p>2. Set up your own cancellation rules.</p>
    <p>3. Enjoy the flexibility to change your rates and charges.</p>
    <p>4. Generate various reports showing booking performances and revenues for any period you desire.</p>
    <p>5. Launch and manage marketing campaigns to increase sales and revenues.</p>
    <p>6. Host and organize tournaments in cooperation with GrassLoop.net.</p>
    <p>7. Identify, target and interact with customers via the social media tools available on GrassLoop.net such as FriendHub and SnapGrid.</p>
  </div>
  <h3 class="tagline">We will do it for you!</h3>
</main>
</body>
</html>
```